KVR Bastion White Paper

We want our text documents to look professional for advertising purposes. We want the White paper to look similar to our Dornwick Basin Study Document attached.

```html
<!DOCTYPE html>
<html lang="en">
<head>
<meta charset="utf-8">
<title>KVR Bastion White Paper</title>
<link rel="stylesheet" href="https://fonts.googleapis.com/css2?family=Tinos:wght@400;700&display=swap">
<style>
:root{
  --backdrop:#e3e3e3;
  --paper:#ffffff;
  --navy:#0d4c97;
  --sky:#1f9ee0;
  --lime:#8cc63f;
  --ink:#3f3f3f;
  --heading:#0d4c97;
  --band:#e6e8ec;
  --rule:#d9d9d9;
  --faint:#c9d3df;
}
*{margin:0;padding:0;box-sizing:border-box}
html,body{width:1200px;height:884px;overflow:hidden;background:var(--backdrop)}
body{position:relative;font-family:"Tinos","Times New Roman",serif;color:var(--ink)}
.page{position:absolute;top:79px;width:512px;height:723px;background:var(--paper);overflow:hidden;box-shadow:0 6px 18px rgba(0,0,0,.12)}
.page--one{left:64px}
.page--two{left:625px}
.header-art{position:absolute;left:0;top:0;width:512px;height:50px}
.brand{position:absolute;left:27px;top:40px;display:flex;align-items:center;gap:5px}
.brand-dot{width:14px;height:14px;border-radius:50%;background:var(--sky)}
.brand-name{font-weight:700;font-size:11px;line-height:11.5px;color:var(--navy)}
.hotline{position:absolute;right:32px;top:64px;font-weight:700;font-size:7.8px;color:var(--heading)}
.block{position:absolute;width:452px;font-size:7.5px;line-height:10.3px;text-align:justify}
.page--one .block{left:30px}
.page--two .block{left:28px}
.block p{text-indent:20px}
.quote{text-indent:0!important}
.divider{position:absolute;left:0;width:512px;height:1px;background:var(--rule)}
.section-head{position:absolute;height:19px;display:flex;align-items:center;width:380px}
.page--one .section-head{left:30px}
.page--two .section-head{left:28px}
.section-num{width:19px;height:19px;background:var(--navy);color:#fff;font-size:11px;display:flex;align-items:center;justify-content:center;flex:none}
.section-title{flex:1;height:19px;margin-left:3px;padding-left:6px;display:flex;align-items:center;font-weight:700;font-size:8.2px;color:var(--heading);background:linear-gradient(90deg,var(--band) 70%,rgba(230,232,236,0))}
.page--two .section-head{width:470px}
.page--two .section-title{background:linear-gradient(90deg,var(--band) 85%,rgba(230,232,236,0))}
.sub-head{position:absolute;height:10px;width:200px;padding-left:6px;font-size:6.2px;line-height:10px;color:#555;background:linear-gradient(90deg,var(--band) 60%,rgba(230,232,236,0))}
.page--one .sub-head{left:46px}
.page--two .sub-head{left:50px}
.refs{position:absolute;left:28px;top:625px;list-style:none;font-size:5.6px;line-height:10.7px;color:var(--navy)}
.refs span{color:#777;display:inline-block;width:8px}
.faint-brand{position:absolute;right:34px;top:638px;display:flex;align-items:center;gap:4px}
.faint-brand .brand-dot{width:10px;height:10px;background:var(--faint)}
.faint-brand .brand-name{font-size:8.2px;line-height:8.6px;font-weight:700;color:var(--faint)}
.folio{position:absolute;left:462px;top:688px;width:18px;height:18px;background:var(--navy);color:#fff;font-size:9px;display:flex;align-items:center;justify-content:center}
.folio-bar{position:absolute;left:462px;top:706px;width:50px;height:7px;background:var(--lime)}
.footer-band{position:absolute;left:0;top:713px;width:512px;height:10px;background:var(--navy)}
</style>
</head>
<body>

<section class="page page--one">
  <svg class="header-art" viewBox="0 0 512 50" aria-hidden="true">
    <rect x="0" y="0" width="160" height="17" fill="#0d4c97"/>
    <rect x="0" y="17" width="512" height="8" fill="#8cc63f"/>
    <path d="M150 0 H166 C182 16 192 34 212 38 H512 V47 H206 C182 44 170 20 150 0 Z" fill="#1f9ee0"/>
  </svg>
  <div class="brand"><span class="brand-dot"></span><span class="brand-name">Dornwick Basin<br>Health Network</span></div>
  <div class="hotline">Have a question? Call 888-555-DBHN (3246)</div>

  <div class="block" style="top:89px">
    <p class="quote">“While advances have been made in infection control practices, including improved operating room ventilation, sterilization methods, barriers, surgical techniques, and availability of antimicrobial prophylaxis, SSIs remain a substantial cause of morbidity, prolonged hospitalization, and death. SSI is associated with a mortality rate of 3% and 75% of SSI associated deaths are directly attributable to SSI.” ~ National Infection Bureau i</p>
  </div>
  <div class="block" style="top:140px">
    <p class="quote">“More than 20,000 deaths per year are due to SSIs, and the chance of death in a surgical patient is doubled if an SSI occurs” ~ Harwell University College of Medicine, Dept. of Surgery ii</p>
  </div>
  <div class="divider" style="top:181px"></div>

  <div class="section-head" style="top:203px"><span class="section-num">I</span><span class="section-title">MAJOR SURGICAL SITE INFECTION PROBLEM IN THE U.S.</span></div>
  <div class="block" style="top:238px">
    <p>America wastes billions of dollars annually on post-operative surgical site infection expenses, especially related to open abdominal surgeries. Surgical site infection (“SSI”) slows the recovery rate for patients and adds additional health costs to facilities with prolonged hospital treatment, additional home care, physician office and emergency room visits expenses.</p>
  </div>
  <div class="block" style="top:279px">
    <p>Open surgeries are more susceptible to high infection rates and slow patient recovery periods which also impact physicians, staff, hospitals, insurers, etc. Moreover, SSI costs hospitals billions of dollars every year in the U.S. and insurance companies do not reimburse hospitals for maladies caused by infection, and corresponding complications due to SSI.</p>
  </div>
  <div class="block" style="top:320px">
    <p>“Surgical site infections (SSI) are among the most common health care-associated infections. Surgical site infections account for 20% to 31% of health care-associated infections in hospitalized patients and have considerable morbidity, a mortality rate of 3%, stays prolonged by 7 to 10 days, and costs $20,000 to $27,000 per admission. Reducing SSIs is a national priority, as reflected in the National Health Office’s National Action Plan to Prevent Healthcare-Associated Infections.” ~ Journal of Clinical Surgical Practice iii</p>
  </div>

  <div class="section-head" style="top:395px"><span class="section-num">II</span><span class="section-title">CURRENT SOLUTIONS</span></div>
  <div class="sub-head" style="top:417px">A. Open Wound and Drainage Treatments</div>
  <div class="block" style="top:441px">
    <p>Surgeons often respond to the high risk of SSI with various open wound and drainage techniques; they do not close the incision area following surgery to allow oxygen into the impacted area. The patient is left with a hole in their body that is open to the outside; restricting patients from normal activity and subjecting them to psychological distress of knowing and often visibly seeing their own open wound. Open wounds require daily wound care cleanings and dressing changes, antibiotics and often high cost wound vac treatments for one to two weeks or longer.</p>
  </div>
  <div class="block" style="top:503px">
    <p>Physicians, in attempts to avoid an open wound, will often install a drainage device either by cutting an additional incision into the patient or by placing a drain laterally inside the wound. This is accomplished by placing a plastic tube into the patient, horizontally along the fascia layer and closing the wound around the tube. The most common drains -- the “J-Drain”, and “Penrose Drain” -- have a tendency to clog up and can even increase the production of additional fluid in patients and consequently the colonization of pathogens, defeating the purpose of the drains. The drains must then be removed by surgeon sometimes a week or more after surgery.</p>
  </div>
  <div class="block" style="top:576px">
    <p>While antibiotics are useful to patient recoveries and are routinely administered prior to and following surgeries, and in conjunction with other preventative measures, pathogens can adapt to antibiotics which has reduced their effectiveness as a preventive measure.</p>
  </div>
  <div class="sub-head" style="top:617px">B. Negative Pressure Therapy Devices</div>
  <div class="block" style="top:641px">
    <p>Recently, “negative pressure therapy” (NPT) devices are often touted as the standard of care for closed incision as well as open wound infection preventative treatments. NPT devices remove excess fluid from surface areas from the outer skin level but can be subject to complications.iv NPT devices are very expensive, physician and nurse-labor intensive, subjected to numerous recalls and often require capital expenditures. In addition, their effectiveness is now being questioned by some clinicians.v</p>
  </div>

  <div class="folio">1</div>
  <div class="folio-bar"></div>
  <div class="footer-band"></div>
</section>

<section class="page page--two">
  <svg class="header-art" viewBox="0 0 512 50" aria-hidden="true">
    <rect x="0" y="0" width="160" height="17" fill="#0d4c97"/>
    <rect x="0" y="17" width="512" height="8" fill="#8cc63f"/>
    <path d="M150 0 H166 C182 16 192 34 212 38 H512 V47 H206 C182 44 170 20 150 0 Z" fill="#1f9ee0"/>
  </svg>
  <div class="brand"><span class="brand-dot"></span><span class="brand-name">Dornwick Basin<br>Health Network</span></div>
  <div class="hotline">Have a question? Call 888-555-DBHN (3246)</div>

  <div class="sub-head" style="top:91px">C. Wound Packing Techniques</div>
  <div class="block" style="top:116px">
    <p>In an attempt to protect their patients, some surgeons use various wound packing techniques to varying degrees of success. These physicians are making their own customized materials, cutting strips and soaking them in various solutions in advance of surgery to protect patients from SSI as best they can. Material retention after surgery is also a concern. While these surgeons are implementing their own materials and methods to help protect their patients, acting on their own they could be placing patients and themselves at additional risk due to non-standardized procedures, material retention, and lack of official oversight.</p>
  </div>

  <div class="section-head" style="top:188px"><span class="section-num">III</span><span class="section-title">A NEW APPROACH IS NEEDED TO LOWER HEALTHCARE COSTS AND REDUCE SSI RATES.</span></div>
  <div class="sub-head" style="top:210px">A. Wound Packing Study</div>
  <div class="block" style="top:233px">
    <p>Dornwick Basin Health network (“Dornwick Study”) conducted a clinical trial on the effectiveness of wound packing. The Dornwick Study involved a high-risk patient group in open colon resection surgeries, a high-risk SSI surgery category, involving a detailed wound packing technique developed over years of case studies. The patient group was comprised of individuals with a variety of high SSI risk factors: steroids/immunosuppressants, some contaminated wounds, blood transfusions, more than 50% had stomas, and an average age of 65.6 and average BMI of 29.</p>
  </div>
  <div class="block" style="top:295px">
    <p>Despite the presence of multiple SSI risk factors and high SSI risk colon sectioning procedures, and the fact that all the patients had their incisions closed with sutures or staples immediately following surgery, the patient group using wound packing resulted in a 2.2% overall infection rate, an 84% reduction in SSI overall, down from 14.2% which was the institution’s control SSI rate. The study had only one case of superficial infection in the study group and zero cases of deep tissue infection.</p>
  </div>
  <div class="block" style="top:347px">
    <p>KVR Bastion™ was designed and developed based on the Dornwick Study, and has been patented and cleared by the national device regulator, and is available for use on clean-contaminated and contaminated wounds and adult patients and pediatrics.</p>
  </div>
  <div class="sub-head" style="top:382px">B. Subcutaneous Dressing Technology: KVR Bastion™</div>
  <div class="block" style="top:405px">
    <p>Subcutaneous dressing technology absorbs fluids from multiple points from the facia layer and above – along the incision site. The subcutaneous dressing transports fluid and debris external to the body and absorbed into the dressing on top of the wound. After the subcutaneous device is removed, the fistulae created by the device forms a channel for the removal of additional fluids and debris.</p>
  </div>
  <div class="block" style="top:446px">
    <p>KVR Bastion™ device is a single-use disposable that features surgical packing strips that are treated with anti-MRSA PHMB Polyhexamethlene Biguanide. With the device, the surgical strips are physically attached to a silver alginate dressing.</p>
  </div>
  <div class="block" style="top:477px">
    <p>KVR Bastion™ is made in the United States. KVR Bastion™ is applied on patients only once immediately following surgery. Packing strips are inserted into the wound and is removed two days later. After that only light dressings and standard wound cleaning methods are employed.</p>
  </div>
  <div class="block" style="top:518px">
    <p>The device can used for clean-contaminated and contaminated incisions. Extra incisions are not needed in the patient, open wound procedures are used only infrequently, and capital rentals and purchases are eliminated.</p>
  </div>
  <div class="block" style="top:549px">
    <p>KVR Bastion can be used on a partial procedure listing including abdominal, trauma and many cancer surgeries, stomach and digestive tract, gallbladder, small intestine, large intestine, appendix, liver, pancreas, esophagus, colon, bladder, prostate, uterus, ovaries, kidney, caesarian section and pediatric procedures.</p>
  </div>
  <div class="divider" style="top:600px"></div>

  <ul class="refs">
    <li><span>i.</span>https://www.infectionbureau.example.org/manual/ssi-current.pdf</li>
    <li><span>ii.</span>https://harwell.example.edu/medicine/departments/surgery/research/surgical-infections-research/</li>
    <li><span>iii.</span>https://clinsurgjournal.example.com/articles/1829988</li>
    <li><span>iv.</span>http://www.woundcarelibrary.example.net/data/editor/NPWT-indications-use-and-possible-complications-review.pdf</li>
    <li><span>v.</span>https://medresearchmethods.example.org/articles/10.1186/1471-2288-8-4</li>
  </ul>
  <div class="faint-brand"><span class="brand-dot"></span><span class="brand-name">Dornwick Basin<br>Health Network</span></div>

  <div class="folio">2</div>
  <div class="folio-bar"></div>
  <div class="footer-band"></div>
</section>

</body>
</html>
```